Maple Crest Glow Skin Studio needs an 8 page WP redesign

We need a colorful re-design for an 8 page Wordpress website. The current preliminary website is live. The home page URL is http://maplecrestglowskinstudio.example The new logo is live on the website also. I would like a (re)design using the colors that are represented by the new logo file, and any additional complimentary colors. The information regarding the business can be found on the website already, so please review it for insight. The name of the business is "Maple Crest Glow Skin Studio".

Target Market(s)

The targeted website viewer is an adult female between the ages of 30 and 75 who is interested in facial renewal, wart removal and scar removal. This website should inspire in the target viewer the benefits of laser facial renewal, wart removal and new scar removal. Potential website viewers are wanting and searching for improved skin health and appearance. The website must represent the essence of a professional spa business.

Industry/Entity Type

Business

Font styles to use
Sans Serif

Requirements
Must have
• - The phone number placed in a visible and high value widget area that allows mobile phone browser dialing.

```html
<!DOCTYPE html>
<html lang="en">
<head>
<meta charset="utf-8">
<title>Maple Crest Glow Skin Studio</title>
<link href="https://fonts.googleapis.com/css2?family=Open+Sans:wght@300;400;600;700&display=swap" rel="stylesheet">
<style>
:root{
  --page:#f3f0e7;
  --purple:#a232ad;
  --purple-dark:#7d2186;
  --ink:#3b3b3b;
  --muted:#9a9a9a;
  --footer:#23272d;
  --footer-text:#d4d6d9;
  --white:#ffffff;
  --rule:#3a3f46;
}
*{box-sizing:border-box;margin:0;padding:0}
html,body{width:1014px;height:1200px;overflow:hidden}
body{background:var(--page);font-family:"Open Sans",Arial,sans-serif;color:var(--ink);position:relative}
.abs{position:absolute}

/* header */
.brand{left:97px;top:40px;display:flex;align-items:center;gap:10px}
.brand-dot{width:34px;height:34px;border-radius:50%;background:var(--purple)}
.brand-name{font-size:21px;font-weight:700;color:var(--purple-dark);line-height:1.15;width:240px}
.social{top:26px;left:654px;display:flex;gap:10px}
.social span{width:20px;height:20px;border-radius:50%;background:var(--purple);display:block}
.social svg{display:block}
.call{right:91px;top:25px;text-align:right;font-size:15px;line-height:19px;color:#555}
.call a{color:var(--purple);text-decoration:none;display:block;padding-right:27px}
.nav{top:82px;left:477px;height:24px;display:flex;font-size:12.5px}
.nav a{color:#666;text-decoration:none;line-height:24px}
.nav .current{background:var(--purple);color:var(--white);width:58px;text-align:center;margin-right:24px}

/* main frame */
.frame{left:93px;top:150px;width:828px;height:1023px;background:var(--white);border:1px solid #e2ddd4}
.grid{left:93px;top:150px;width:828px;height:414px;display:grid;grid-template-columns:repeat(4,207px);grid-template-rows:repeat(2,207px)}
.photo{width:207px;height:207px}
.feature{background:var(--purple);color:var(--white);padding:22px 10px 0 7px;position:relative}
.feature h3{font-size:15px;font-weight:600;margin-bottom:14px}
.feature p{font-size:10.5px;line-height:17px;padding-left:2px}
.feature svg{position:absolute;left:91px;top:174px}

.welcome{left:110px;top:590px;width:504px}
.welcome h1{font-size:21px;font-weight:300;color:#444;letter-spacing:-0.3px}
.welcome h1 strong{font-weight:600;color:var(--purple)}
.welcome p{font-size:10.6px;line-height:17.7px;color:var(--muted);margin-top:10px}
.welcome p+p{margin-top:10px}
.book{left:111px;top:823px;width:115px;height:34px;background:var(--purple);color:var(--white);font-size:15px;font-weight:600;border-radius:2px;border:1px solid var(--purple-dark);text-align:center;line-height:32px}

.carousel{left:650px;top:591px;width:234px;height:234px;border-radius:50%;background:#eeeeee;padding:6px}
.carousel div{width:100%;height:100%;border-radius:50%;background:linear-gradient(160deg,#e9dfd6,#d9a98f 45%,#f1c6cf)}
.arrow{width:42px;height:42px;border-radius:50%;background:#e2e2e2;padding:4px}
.arrow svg{display:block}
.select{left:600px;top:840px;width:333px;text-align:center;font-size:13px;color:#444}

/* newsletter */
.newsletter{left:93px;top:888px;width:828px;height:67px;background:var(--purple);color:var(--white)}
.newsletter h2{position:absolute;left:13px;top:11px;font-size:16px;font-weight:600}
.newsletter p{position:absolute;left:13px;top:34px;font-size:10px}
.field{position:absolute;top:23px;width:178px;height:26px;background:var(--white);border:2px solid #d9d9d9;font-size:9px;color:#aaa;padding:6px 7px}
.subscribe{position:absolute;left:706px;top:20px;width:107px;height:32px;background:#111;border-radius:3px;color:var(--white);font-size:14px;font-weight:600;text-align:center;line-height:32px}

/* footer */
.footer{left:93px;top:955px;width:828px;height:218px;background:var(--footer);color:var(--footer-text)}
.col{position:absolute;top:19px}
.col h4{font-size:13px;font-weight:400;color:var(--white);margin-bottom:12px}
.col li{list-style:none;font-size:10.5px;line-height:19.5px}
.divider{position:absolute;top:51px;width:1px;height:110px;background:var(--rule)}
.testimonial{display:flex;gap:10px}
.avatar{width:38px;height:38px;background:linear-gradient(#b9b3ad,#6d6660);flex:none;margin-top:2px}
.testimonial .who{color:var(--purple);font-size:10px;margin-bottom:6px;display:block;padding-left:2px}
.testimonial q{font-size:10.5px;line-height:17px;display:block;width:190px}
.bottom{position:absolute;left:0;top:176px;width:828px;border-top:1px solid var(--rule);padding-top:12px;font-size:10.5px;display:flex;justify-content:space-between}
</style>
</head>
<body>

<header>
  <div class="abs brand"><span class="brand-dot"></span><span class="brand-name">Maple Crest Glow Skin Studio</span></div>
  <div class="abs social">
    <span aria-label="Social profile"></span>
    <span aria-label="Social profile"></span>
    <span aria-label="Search"><svg width="20" height="20" viewBox="0 0 20 20"><circle cx="9" cy="9" r="4" fill="none" stroke="#fff" stroke-width="2"/><line x1="12" y1="12" x2="15" y2="15" stroke="#fff" stroke-width="2.2" stroke-linecap="round"/></svg></span>
  </div>
  <div class="abs call">YOU CALL, WE'RE THERE<a href="tel:08005550199">(0800-555-0199)</a></div>
  <nav class="abs nav">
    <a class="current" href="#">Home</a>
    <a href="#" style="margin-right:36px">About Us</a>
    <a href="#" style="margin-right:36px">The Clinic</a>
    <a href="#" style="margin-right:36px">Services</a>
    <a href="#" style="margin-right:36px">Blog</a>
    <a href="#">Contact</a>
  </nav>
</header>

<div class="abs frame"></div>

<section class="abs grid">
  <div class="photo" role="img" aria-label="Portrait of a woman with flowers" style="background:linear-gradient(135deg,#f6e2cc,#efc9b5 55%,#dcb6a4)"></div>
  <div class="photo feature">
    <h3>Wart Renewal</h3>
    <p>Lorem ipsum dolor sit amet, consecte-tur adipisicing elit, sed do eiusmod tempor incididunt ut labore et dolore magna aliqua.</p>
    <svg width="25" height="25" viewBox="0 0 25 25"><circle cx="12.5" cy="12.5" r="12.5" fill="#fff"/><path d="M7 10.5h6v-4l6 6-6 6v-4H7z" fill="#a232ad"/></svg>
  </div>
  <div class="photo" role="img" aria-label="Woman holding a flower" style="background:linear-gradient(135deg,#cfe6c8,#f4d6d2 50%,#f1b9cc)"></div>
  <div class="photo" role="img" aria-label="Facial skin treatment with a device" style="background:linear-gradient(160deg,#e9d7bf,#d7a57d 55%,#f0d46a)"></div>
  <div class="photo" role="img" aria-label="Laser device on skin" style="background:linear-gradient(135deg,#e6b59c,#6c5a52 60%,#3c3b3e)"></div>
  <div class="photo" role="img" aria-label="Relaxing spa massage" style="background:linear-gradient(150deg,#b69b8f,#dcb39c 55%,#f0d3a8)"></div>
  <div class="photo" role="img" aria-label="Laser treatment on legs" style="background:linear-gradient(150deg,#9a9793,#e3b99f 50%,#f3d5da)"></div>
  <div class="photo" role="img" aria-label="Facial massage" style="background:linear-gradient(160deg,#e4b8a0,#f2d8c8 55%,#f6efe9)"></div>
</section>

<section class="abs welcome">
  <h1>Welcome to the <strong>MAPLE CREST GLOW SKIN STUDIO</strong></h1>
  <p>Lorem Ipsum est simplement du faux texte employé dans la sition et la misen page avant impres-sion. Le Lorem Ipsum est le faux texte standard de l'imprimerie depuis les années 1500, quand un peintre anonyme assembla ensemble des morceaux de texte pour réaliser un livre spécimen de polices de texte.</p>
  <p>Il n'a pas fait que survivre cinq siècles, mais s'est aussi adapté à la bureautique informatique, sans que son contenu n'en soit modifié. Il a été popularisé dans les années 1960.<br>&nbsp;grâce à la vente de feuilles Letraset contenant Le Lorem Ipsum est le faux texte standard de l'imprimerie depuis les années 1500, quand un peintre anonyme assembla ensemble des morceaux de texte pour réaliser un livre spécimen...</p>
</section>
<a class="abs book">Book Online</a>

<div class="abs carousel"><div role="img" aria-label="Laser leg treatment in progress"></div></div>
<div class="abs arrow" style="left:636px;top:687px"><svg width="34" height="34" viewBox="0 0 34 34"><circle cx="17" cy="17" r="17" fill="#3b3d40"/><path d="M20 10l-7 7 7 7" fill="none" stroke="#fff" stroke-width="2"/></svg></div>
<div class="abs arrow" style="left:860px;top:687px"><svg width="34" height="34" viewBox="0 0 34 34"><circle cx="17" cy="17" r="17" fill="#3b3d40"/><path d="M14 10l7 7-7 7" fill="none" stroke="#fff" stroke-width="2"/></svg></div>
<div class="abs select">SELECT YOUR GLOW SKIN TREATMENT</div>

<section class="abs newsletter">
  <h2>SIGN UP TO A NEWSLETTER</h2>
  <p>Lorem ipsum dolor sit amet, consectetur adipisicing elit...</p>
  <div class="field" style="left:319px">NAME...</div>
  <div class="field" style="left:511px">EMAIL...</div>
  <div class="subscribe">SUBCRIBE</div>
</section>

<footer class="abs footer">
  <div class="col" style="left:14px">
    <h4>SITE LINKS</h4>
    <ul><li>Home</li><li>About Us</li><li>Skin Renewal</li><li>Services</li><li>blog</li><li>Contact Us</li></ul>
  </div>
  <div class="divider" style="left:159px"></div>
  <div class="col" style="left:212px">
    <h4>ABOUT US</h4>
    <ul><li>Lorem Ipsum</li><li>Dolor Sit Amet</li><li>Consectetur</li><li>Adipsicing Elit.</li></ul>
  </div>
  <div class="divider" style="left:320px"></div>
  <div class="col" style="left:360px">
    <h4>TESTIMONIALS</h4>
    <div class="testimonial">
      <div class="avatar" role="img" aria-label="Customer portrait"></div>
      <div><span class="who">Corwin Abbott</span><q>Lotrem ipsum dolor sit nsectetuer adipiscing elit, sed diam nummy nibh euismod.ut laoreet dolore magna aliquam rat volutpat. Ut wisi enim ad minim.</q></div>
    </div>
  </div>
  <div class="divider" style="left:612px"></div>
  <div class="col contact" style="left:648px">
    <h4>CONTACT INFORMATIONS:</h4>
    <ul><li>Address: Lorem ipsum dolor</li><li>Street,123</li><li>E-mail:</li><li>info@maplecrestglow.example</li><li>Phone: +47 55 01 02 03</li></ul>
  </div>
  <div class="bottom"><span>Copyright 2015 MAPLE CREST GLOW SKIN STUDIO. All Rights Reserved.</span><span>Privacy Policy I Terms &amp; Condition</span></div>
</footer>

</body>
</html>
```